Auto Tuning Shop needs an advertising design

An advertising design that can be used online for marketing on Pagelore, Quorvex, Snapwillow. A picture that says exactly what we do - window tinting / car window films. Looks professional and is informative. But not too much content and text.
Possibly a picture of the car looks like window tint from the outside (very dark), but when sitting in the car you have a perfect view of the outside.
Passwords in picture: UV protection, heat protection, burglary protection, privacy protection
Not too many colors.

Here are a few sample pictures as we often designed it ourselves, but it has to look more professional.

Target Market(s)

Reach new customers because it is a campaign / offer

Requirements
Must have
• German language
Nice to have
• Passwords in picture: UV protection, heat protection, burglary protection, privacy protection

```html
<!DOCTYPE html>
<html lang="de">
<head>
<meta charset="utf-8">
<title>KLARVO – Professionelle Scheibentönung</title>
<link rel="stylesheet" href="https://fonts.googleapis.com/css2?family=Oswald:wght@600&family=Lato:ital,wght@0,400;0,700;0,900;1,400&display=swap">
<style>
  :root{
    --stage:#8e8e8e;
    --ink:#0b0b0b;
    --header:#2a2a2a;
    --red:#e3202a;
    --red-dark:#8a1a1d;
    --gold:#c9a43a;
    --gold-light:#f0d27a;
    --white:#ffffff;
    --tile:#b7b7b7;
    --rule:#6a6a6a;
  }
  html,body{margin:0;padding:0;overflow:hidden}
  body{width:1200px;height:1200px;background:var(--stage);position:relative}
  .banner{position:absolute;left:40px;top:258px;width:1120px;height:683px;display:block}
  .title{font-family:"Oswald",sans-serif;font-weight:600;fill:var(--white)}
  .tagline{font-family:"Lato",sans-serif;font-weight:700;fill:var(--white)}
  .brand{font-family:"Lato",sans-serif;font-weight:900;fill:var(--red)}
  .label{font-family:"Lato",sans-serif;font-weight:700;fill:#7a1c14}
  .contact{font-family:"Lato",sans-serif;font-weight:400;fill:var(--white)}
  .web{font-family:"Lato",sans-serif;font-weight:900;fill:var(--ink)}
  .feature{font-family:"Lato",sans-serif;font-style:italic;font-weight:400;fill:var(--white)}
</style>
</head>
<body>
<svg class="banner" viewBox="0 0 1014 618" xmlns="http://www.w3.org/2000/svg">
  <defs>
    <linearGradient id="tag-band" x1="0" x2="1">
      <stop offset="0" stop-color="#2a1010"/><stop offset="1" stop-color="var(--red)"/>
    </linearGradient>
    <linearGradient id="feature-panel" x1="0" x2="1">
      <stop offset="0" stop-color="#1a1a1a"/><stop offset="0.55" stop-color="#5a1c1e"/><stop offset="1" stop-color="#c0272d"/>
    </linearGradient>
    <linearGradient id="gold-bar" x1="0" x2="1">
      <stop offset="0" stop-color="var(--gold-light)"/><stop offset="0.6" stop-color="var(--gold)"/><stop offset="1" stop-color="#1a1a1a"/>
    </linearGradient>
    <linearGradient id="car-photo" x1="0" x2="1" y1="0" y2="1">
      <stop offset="0" stop-color="#6e6a62"/><stop offset="0.5" stop-color="#7c8288"/><stop offset="1" stop-color="#3a3d40"/>
    </linearGradient>
    <linearGradient id="interior-photo" x1="0" x2="1">
      <stop offset="0" stop-color="#c9a27a"/><stop offset="0.45" stop-color="#3a2c24"/><stop offset="1" stop-color="#a9c2d6"/>
    </linearGradient>
  </defs>

  <!-- base -->
  <rect class="base" width="1014" height="618" fill="var(--ink)"/>

  <!-- header -->
  <polygon class="header" points="258,0 1014,0 1014,86 318,86" fill="var(--header)"/>
  <text class="title" x="665" y="68" font-size="54" text-anchor="middle" textLength="642" lengthAdjust="spacingAndGlyphs">PROFESSIONELLE SCHEIBENTÖNUNG</text>
  <line x1="318" y1="86" x2="1014" y2="86" stroke="var(--gold)" stroke-width="3"/>

  <!-- tagline band -->
  <polygon points="318,88 1014,88 1014,135 350,135" fill="url(#tag-band)"/>
  <text class="tagline" x="760" y="121" font-size="25" text-anchor="middle">✦GERMAN QUALITY OF WINDOW✦</text>

  <!-- photos -->
  <polygon role="img" aria-label="Foto: graue Limousine mit dunkel getönten Scheiben, Heckansicht" points="0,158 360,158 455,372 0,372" fill="url(#car-photo)"/>
  <polygon role="img" aria-label="Foto: Frau im Auto blickt durch die getönte Seitenscheibe nach draußen" points="500,158 1014,158 1014,372 590,372" fill="url(#interior-photo)"/>

  <!-- red diagonal stripe -->
  <polygon class="stripe" points="235,0 258,0 350,135 500,158 620,372 470,372 360,158" fill="var(--red)"/>

  <!-- gold divider -->
  <line x1="0" y1="372" x2="1014" y2="372" stroke="var(--gold)" stroke-width="4"/>

  <!-- feature panel -->
  <polygon points="470,374 1014,374 1014,618 620,618" fill="url(#feature-panel)"/>
  <polygon points="300,374 470,374 620,618 450,618" fill="var(--red)"/>

  <!-- brand -->
  <circle cx="52" cy="72" r="10" fill="var(--gold)"/>
  <text class="brand" x="72" y="86" font-size="42">KLARVO</text>

  <!-- contact -->
  <polygon points="50,380 320,380 340,414 50,414" fill="url(#gold-bar)"/>
  <text class="label" x="85" y="404" font-size="21">Sie finden uns hier:</text>

  <g class="contact-icons" fill="var(--gold)">
    <path d="M76,444 l4,-2 3,5 -2,2 q2,4 6,6 l2,-2 5,3 -2,4 q-10,0 -16,-16z"/>
    <path d="M80,466 a6,6 0 0 1 12,0 q0,5 -6,12 q-6,-7 -6,-12z"/>
    <circle cx="86" cy="466" r="2" fill="var(--ink)"/>
    <rect x="74" y="519" width="15" height="10" fill="none" stroke="var(--gold)" stroke-width="1.5"/>
    <path d="M74,519 l7.5,6 7.5,-6" fill="none" stroke="var(--gold)" stroke-width="1.5"/>
  </g>
  <text class="contact" x="95" y="459" font-size="19">0151 48213 906</text>
  <text class="contact" x="95" y="483" font-size="19">Birkenallee 7,</text>
  <text class="contact" x="95" y="507" font-size="19">80999 Musterstadt - Nord</text>
  <text class="contact" x="95" y="531" font-size="19">info@klarvo.de</text>

  <!-- web bar -->
  <polygon points="0,565 90,565 90,600 0,600" fill="var(--red)"/>
  <polygon points="90,565 420,565 440,600 90,600" fill="url(#gold-bar)"/>
  <circle cx="63" cy="582" r="8" fill="none" stroke="var(--white)" stroke-width="2"/>
  <line x1="55" y1="582" x2="71" y2="582" stroke="var(--white)" stroke-width="1.5"/>
  <line x1="63" y1="574" x2="63" y2="590" stroke="var(--white)" stroke-width="1.5"/>
  <text class="web" x="96" y="590" font-size="22">www.klarvo.de</text>

  <!-- features -->
  <g class="features">
    <line x1="520" y1="440" x2="1004" y2="440" stroke="var(--rule)" stroke-width="1.5"/>
    <line x1="555" y1="495" x2="1004" y2="495" stroke="var(--rule)" stroke-width="1.5"/>
    <line x1="590" y1="550" x2="1004" y2="550" stroke="var(--rule)" stroke-width="1.5"/>

    <polygon class="tile" points="437,390 502,390 528,436 463,436" fill="var(--tile)"/>
    <circle cx="484" cy="403" r="8" fill="var(--ink)"/>
    <text x="484" y="407" font-family="Lato,sans-serif" font-size="9" font-weight="900" fill="var(--tile)" text-anchor="middle">UV</text>
    <rect x="468" y="415" width="32" height="4" fill="var(--ink)"/>
    <rect x="468" y="422" width="32" height="6" fill="var(--ink)"/>
    <text class="feature" x="553" y="423" font-size="26">UV-Schutz</text>

    <polygon class="tile" points="472,445 537,445 563,491 498,491" fill="var(--tile)"/>
    <circle cx="517" cy="468" r="8" fill="var(--ink)"/>
    <g stroke="var(--ink)" stroke-width="2.5">
      <line x1="517" y1="453" x2="517" y2="457"/><line x1="517" y1="479" x2="517" y2="483"/>
      <line x1="502" y1="468" x2="506" y2="468"/><line x1="528" y1="468" x2="532" y2="468"/>
      <line x1="506" y1="457" x2="509" y2="460"/><line x1="525" y1="476" x2="528" y2="479"/>
      <line x1="528" y1="457" x2="525" y2="460"/><line x1="509" y1="476" x2="506" y2="479"/>
    </g>
    <text class="feature" x="587" y="478" font-size="26">Hitzeschutz</text>

    <polygon class="tile" points="506,500 571,500 597,546 532,546" fill="var(--tile)"/>
    <path d="M537,507 l15,5 v10 q0,12 -15,18 q-15,-6 -15,-18 v-10z" fill="var(--ink)"/>
    <ellipse cx="537" cy="523" rx="8" ry="4.5" fill="var(--tile)"/>
    <circle cx="537" cy="523" r="2.5" fill="var(--ink)"/>
    <text class="feature" x="617" y="533" font-size="26">Sichtschutz &amp; Splitterschutz</text>

    <polygon class="tile" points="541,555 606,555 632,601 567,601" fill="var(--tile)"/>
    <rect x="560" y="574" width="24" height="18" rx="2" fill="var(--ink)"/>
    <path d="M565,574 v-6 a7,7 0 0 1 14,0 v6" fill="none" stroke="var(--ink)" stroke-width="3"/>
    <circle cx="572" cy="582" r="2.5" fill="var(--tile)"/>
    <text class="feature" x="653" y="588" font-size="26">Einbruchschutz</text>
  </g>
</svg>
</body>
</html>
```